Create Brightquill's (yes, OUR) Office Door!

We are looking to spruce up the old office here at Brightquill, and why not use our amazing designers for the project!
This design will be viewed by our employees everyday :) and will be in our doorway leading to the office. See the photo attached as well as the dimensions.
NOTE THE UPDATES PLEASE AS OF NOV 8, 10 AM Australian time!!
The designs should be 1 color (probably white on top of grey), the background color remain dark grey. The logo should be prominent, and CAN be modified a bit (e.g. with sketch style of the character attached).
Updates
We've received some good designs, so far thanks for submitting! Here are 2 pieces of advice
Thanks,
About 33% of you included the design on the door. As pictured the door is always open so is not part of the canvas. See the new dimensions, which is 595mm X 2000mm
Thanks
Reason: We've got some great designs but would love to see more!
Industry/Entity Type
Office
Requirements
Must have
- Brightquill name (Vertical length or horizontal, both options)?
The Brightquill logo
(NOTE: Measurements & actual photos attached) - NOTE THE UPDATE AS WELL with dimensions. It is now 595mm X 2000 mm only on the right side.
Nice to have
- Sketch-Style graphic (a few options included)
Arrow with the Boopee font type with text:"Faster. Better. More Creative."
Incorporate creative "door entry" concepts. Come up with your own creatives! That will be key for us to choose a winner - incorporate creativity. Here are some ideas:
1) Keypad for security entry
2) Security camera in top right corner with a message between hip & eye level "Look up for eye scan"
3) Place to put hand for laser scan
etc.
Creativity required :)
Should not have
- It should not be too "busy" and have too much going on. Close your eyes and imagine walking past this, you should be able to see everything in a quick glance and maybe even say "ah that's nice" before you start your day/meeting/interview to work here.

```html
<!DOCTYPE html>
<html lang="en">
<head>
<meta charset="utf-8">
<title>Brightquill Office Door – Lab 001</title>
<link rel="stylesheet" href="https://fonts.googleapis.com/css2?family=Bebas+Neue&display=swap">
<style>
  :root {
    --backdrop: #0b5b7b;
    --panel-light: #ffffff;
    --panel-light-edge: #dcdcdc;
    --wall: #252525;
    --door: #262626;
    --door-frame: #1c1c1c;
    --ink-dark: #111111;
    --ink-light: #ffffff;
    --window-frame: #151515;
  }
  * { margin: 0; padding: 0; box-sizing: border-box; }
  html, body { width: 1200px; height: 849px; overflow: hidden; }
  body {
    position: relative;
    background: var(--backdrop);
    font-family: "Bebas Neue", "Arial Narrow", sans-serif;
  }
  .door-view { position: absolute; }

  /* Light door option */
  .door-light {
    left: 54px; top: 196px; width: 389px; height: 581px;
    background: linear-gradient(90deg, var(--panel-light) 0%, var(--panel-light) 35%, var(--panel-light-edge) 100%);
    box-shadow: 0 2px 6px rgba(0,0,0,.35);
  }

  /* Dark wall with door */
  .wall-dark {
    left: 477px; top: 71px; width: 662px; height: 706px;
    background: var(--wall);
  }
  .door-dark {
    left: 477px; top: 183px; width: 414px; height: 594px;
    background: var(--door-frame);
    padding: 11px 12px 0 11px;
    box-shadow: 0 -1px 0 #333;
  }
  .door-dark .door-leaf {
    width: 100%; height: 100%;
    background: var(--door);
    box-shadow: inset 0 0 0 1px #2e2e2e, 2px 0 4px rgba(0,0,0,.5);
    position: relative;
  }

  .door-window {
    position: absolute;
    width: 75px; height: 208px;
    background: var(--window-frame);
    padding: 10px 9px;
    box-shadow: 2px 3px 5px rgba(0,0,0,.45);
  }
  .door-window .glass {
    width: 100%; height: 100%;
    background:
      linear-gradient(160deg, transparent 0 30%, rgba(255,255,255,.55) 31%, rgba(255,255,255,.15) 55%, transparent 70%),
      linear-gradient(180deg, #000 0%, #333 45%, #aaa 70%, #222 100%);
  }
  .door-light .door-window { left: 90px; top: 65px; }
  .door-dark .door-window { left: 224px; top: 67px; }

  .room-title {
    position: absolute; width: 100%;
    text-align: center;
    font-size: 118px; line-height: 1;
    letter-spacing: 2px;
  }
  .room-motto {
    position: absolute; width: 100%;
    text-align: center;
    font-size: 27px; line-height: 1;
    letter-spacing: .5px;
  }
  .door-light .room-title { top: 310px; color: var(--ink-dark); }
  .door-light .room-motto { top: 428px; color: var(--ink-dark); }
  .door-dark .room-title { top: 313px; color: var(--ink-light); }
  .door-dark .room-motto { top: 431px; color: var(--ink-light); }

  .caution-line {
    position: absolute; left: 527px; top: 118px;
    color: var(--ink-light);
    font-size: 33px; line-height: 1; letter-spacing: .5px;
  }

  .brand-mark {
    position: absolute; left: 928px; top: 98px;
    width: 60px; height: 60px; border-radius: 50%;
    background: var(--ink-light);
  }
  .brand-name {
    position: absolute; left: 905px; top: 190px;
    width: 110px; height: 550px;
    writing-mode: vertical-rl;
    transform: rotate(180deg);
    color: var(--ink-light);
    font-size: 126px; line-height: 110px;
    text-align: center;
    letter-spacing: 1px;
  }
</style>
</head>
<body>
  <div class="door-view door-light">
    <div class="door-window"><div class="glass"></div></div>
    <p class="room-title">LAB 001</p>
    <p class="room-motto">FOLLOW YOUR OWN PATH ONLY</p>
  </div>

  <div class="door-view wall-dark"></div>
  <p class="caution-line">CAUTION! CREATIVE MATERIALS</p>
  <div class="brand-mark" aria-hidden="true"></div>
  <p class="brand-name">Brightquill</p>

  <div class="door-view door-dark">
    <div class="door-leaf">
      <div class="door-window"><div class="glass"></div></div>
      <p class="room-title">LAB 001</p>
      <p class="room-motto">FOLLOW YOUR OWN PATH ONLY</p>
    </div>
  </div>
</body>
</html>
```